Concept design for a tea business Labels

Hello, we are looking for concepts for our label/packaging for a tea business that has been in business now for over a year. We are a beachy, organic, "It's your moment. Enjoy it." type tea business. We have an online website (www.driftleafbrews.com.au) and sell at local markets around the Corvel Cove area.
We are looking to upgrade our label to look more professional, in a fun/beachy/chilled out style. (unlike the traditional tea labels).
We do loose leaf tea and iced tea consentrated syrups. We have a few different packages (please see website under "sizes and packaging" bottom left). We would like to experiement with various different size and shape of labels for different products, so would like a concept design for a label using our logo (see website front page bottom). There are no colour constraints.
We use the Norvik brand labels of the following sizes:
1. Pure Glint Rectangular Product Labels, Q4826, 100/Pack, 96 x 50.8 mm
2. Pure Glint Round Multi-purpose Labels, Q3957D, 240/Pack, 40 mm diameter
3.Pure Glint Square Product Labels, Q4861, 350/Pack, 35 x 35 mm
4. For bottles we use Grained Ivory Domed Labels, Q4839, 90/Pack, 57.2 x 77 mm
If you have any more questions, please don't hesitate to contact me
Updates
Hi All,
I am considering using a box like below for packing and doing a bit of a white/beachy feel to the packaging. Either using the rectangle or round circle labels. (circle labels from norvik 60mm diameter).

Reason: Hi All - Thank you so much for all your designs. While I have seen some really beautiful designs I am excited about, it seems there was a rush at the end with a number of new designs just submitted. I still haven't seen just one design I love for the label, so I would like the opportunity to work with some of the new designers to see if we can modify to suit the concept.
Would anyone like to try a concept label with a silhouette of one of the following wave/beach/teacup? I'm just exploring a different approach as I know it is difficult tying in the beach with tea - please think - chilled out beach hut with tea/iced tea, sunrise over ocean. I like the soft colour palette - beachy feel to it - ie. Pastels - blues, greens, whites, sandy, pinks, purples, greys - sunrises over ocean, maybe a white rustic wood feel - or any other icon from Corvel Cove - like the Norfolk Pine's along the beach - maybe in Silhouette.
Just some more ideas.
Thank you again for all your contributions!
Greta

```html
<!DOCTYPE html>
<html lang="en">
<head>
<meta charset="utf-8">
<title>Corvel Tea Company – Label Concepts</title>
<link rel="stylesheet" href="https://fonts.googleapis.com/css2?family=Oswald:wght@300;400;500;600&family=Righteous&display=swap">
<style>
  :root {
    --sand: #dccb98;
    --sand-deep: #cdb983;
    --plum: #52365f;
    --olive: #4a4a2c;
    --slate-blue: #4a6585;
    --orange: #f47c3c;
    --orange-deep: #c4541c;
    --cream: #f4ead0;
    --leaf-mauve: #a59282;
    --leaf-sage: #9fa37d;
    --leaf-teal: #7f9a8a;
    --ink-plum: #4b3458;
    --ink-olive: #3f3f26;
    --ink-navy: #3a4a60;
  }
  * { box-sizing: border-box; margin: 0; padding: 0; }
  html, body { width: 1200px; height: 1000px; overflow: hidden; background: #ffffff; }
  body { position: relative; font-family: "Oswald", sans-serif; }

  .label { position: absolute; overflow: hidden; background: var(--sand); text-align: center; }
  .label--round { border-radius: 50%; }
  .label--lemongrass { left: 50px; top: 46px; width: 424px; height: 424px; border: 4px solid var(--plum); }
  .label--oolong { left: 28px; top: 504px; width: 420px; height: 420px; border: 4px solid var(--olive); }
  .label--bottle { left: 715px; top: 45px; width: 355px; height: 478px; border-radius: 178px 178px 0 0; }

  .botanical { position: absolute; border-radius: 45% 45% 10% 10%; }
  .label--lemongrass .botanical { left: 60px; top: 70px; width: 300px; height: 330px;
    background: radial-gradient(ellipse at 50% 60%, var(--leaf-mauve) 0%, rgba(165,146,130,0.5) 45%, rgba(220,203,152,0) 72%); }
  .label--oolong .botanical { left: 50px; top: 60px; width: 320px; height: 330px;
    background: radial-gradient(ellipse at 50% 60%, var(--leaf-sage) 0%, rgba(159,163,125,0.5) 45%, rgba(220,203,152,0) 72%); }
  .label--bottle .botanical { left: 20px; top: 40px; width: 320px; height: 420px;
    background: radial-gradient(ellipse at 50% 55%, var(--leaf-teal) 0%, rgba(127,154,138,0.5) 45%, rgba(220,203,152,0) 72%); }

  .brand-mark { position: absolute; left: 50%; transform: translateX(-50%); display: flex; flex-direction: column; align-items: center; gap: 4px; }
  .brand-mark__dot { width: 58px; height: 58px; border-radius: 50%; background: var(--orange); }
  .brand-mark__name { font-weight: 500; font-size: 18px; color: var(--orange); letter-spacing: 1px; }
  .label--lemongrass .brand-mark { top: 40px; }
  .label--oolong .brand-mark { top: 40px; }
  .label--bottle .brand-mark { top: 60px; }

  .company { position: absolute; left: 0; right: 0; font-weight: 400; font-size: 20px; transform: scaleX(0.88); }
  .label--lemongrass .company { top: 180px; color: var(--ink-plum); }
  .label--oolong .company { top: 173px; color: var(--ink-olive); }
  .label--bottle .company { top: 193px; color: var(--ink-navy); font-size: 19px; }

  .product-name { position: absolute; left: 0; right: 0; font-weight: 600; color: var(--orange);
    text-shadow: 1px 1px 0 var(--orange-deep), 2px 3px 3px rgba(60,40,30,0.55); }
  .label--lemongrass .product-name { top: 208px; font-size: 37px; letter-spacing: 1px; }
  .label--oolong .product-name { top: 206px; font-size: 48px; letter-spacing: 1px; }

  .ingredients-line { position: absolute; left: 0; right: 0; top: 278px; font-weight: 400; font-size: 12px;
    letter-spacing: 3px; color: var(--ink-plum); }

  .weight { position: absolute; left: 0; right: 0; font-weight: 400; letter-spacing: 2px; }
  .label--oolong .weight { top: 292px; font-size: 20px; color: var(--ink-olive); }

  .band { position: absolute; left: 0; right: 0; bottom: 0; display: flex; justify-content: center; color: var(--cream); }
  .label--lemongrass .band { height: 78px; background: var(--plum); padding-top: 17px; font-size: 20px; letter-spacing: 2px; }
  .label--oolong .band { height: 70px; background: var(--olive); padding-top: 16px; font-size: 19px; letter-spacing: 2px; }
  .label--bottle .band { height: 73px; background: var(--slate-blue); flex-direction: column; align-items: center; padding-top: 10px; }

  .volume { position: absolute; right: 30px; top: 127px; font-size: 17px; color: var(--ink-navy); letter-spacing: 1px; }
  .iced-title { position: absolute; left: 0; right: 0; top: 226px; font-family: "Righteous", sans-serif; font-size: 40px;
    color: #ffffff; letter-spacing: 2px; text-shadow: 1px 2px 2px rgba(40,50,60,0.5); }
  .info { position: absolute; top: 276px; width: 120px; font-weight: 300; font-size: 13px; line-height: 18px;
    color: var(--ink-navy); text-align: left; }
  .info h3 { font-weight: 400; font-size: 13px; text-align: center; }
  .info--ingredients { left: 40px; }
  .info--directions { left: 227px; }
  .flavour { font-family: "Righteous", sans-serif; font-size: 25px; letter-spacing: 1px; color: var(--orange);
    text-shadow: 1px 1px 0 var(--orange-deep); }
  .website { font-weight: 400; font-size: 17px; color: var(--cream); transform: scaleX(0.9); }
</style>
</head>
<body>

  <section class="label label--round label--lemongrass">
    <div class="botanical" role="img" aria-label="Soft mauve silhouette of lemongrass and ginger leaves"></div>
    <div class="brand-mark"><span class="brand-mark__dot"></span><span class="brand-mark__name">Corvel</span></div>
    <p class="company">CORVEL TEA COMPANY</p>
    <h2 class="product-name">Lemongrass &amp; Ginger</h2>
    <p class="ingredients-line">organic lemongrass, organic ginger</p>
    <div class="band">200 grms</div>
  </section>

  <section class="label label--bottle">
    <div class="botanical" role="img" aria-label="Soft teal silhouette of tea leaves with bubbles"></div>
    <div class="brand-mark"><span class="brand-mark__dot"></span><span class="brand-mark__name">Corvel</span></div>
    <p class="volume">250ml</p>
    <p class="company">CORVEL TEA COMPANY</p>
    <h2 class="iced-title">ICED TEA</h2>
    <div class="info info--ingredients">
      <h3>Ingredients</h3>
      <p>raw sugar, organic green tea, fresh orange juice, lemon juice, potassium sorbate, elderberry juice.</p>
    </div>
    <div class="info info--directions">
      <h3>Directions</h3>
      <p>raw sugar, organic green tea, fresh orange juice, lemon juice, potassium sorbate, elderberry juice.</p>
    </div>
    <div class="band">
      <span class="flavour">BLOOD ORANGE</span>
      <span class="website">www.driftleafbrews.com.au</span>
    </div>
  </section>

  <section class="label label--round label--oolong">
    <div class="botanical" role="img" aria-label="Soft sage silhouette of oolong tea leaves"></div>
    <div class="brand-mark"><span class="brand-mark__dot"></span><span class="brand-mark__name">Corvel</span></div>
    <p class="company">CORVEL TEA COMPANY</p>
    <h2 class="product-name">Milky Oolong</h2>
    <p class="weight">200 grms</p>
    <div class="band">organic tea</div>
  </section>

</body>
</html>
```